Quote Cards With TK May 2025 for Instagram

I would like to put these quotes over one of the pictures attached; Instagram (new size: 4:5 (1080 x 1350 pixels) One Quote per picture, and I want the quote to be bold or easy to read as well. I provided a few reference graphics that I really like as examples below. In very small letters at the bottom add @TKBarlowOnline

All of the pictures are attached; you can pick any photo and add one quote to it; but no stock photography

```html
<!DOCTYPE html>
<html lang="en">
<head>
<meta charset="utf-8">
<title>Quote Cards with TK – May 2025</title>
<link href="https://fonts.googleapis.com/css2?family=Montserrat:wght@500;700;800&display=swap" rel="stylesheet">
<style>
  :root{
    --stage:#cbcbcb;
    --white:#ffffff;
    --muted:#b9b3c4;
    --lavender:#c7bfe0;
    --olive:#a6ad7c;
    --pink:#e27ac0;
    --rose:#d891b4;
    --tan:#d9b99b;
    --handle:#d8d8d8;
  }
  *{box-sizing:border-box;margin:0;padding:0}
  html,body{width:1200px;height:376px;overflow:hidden;background:var(--stage)}
  body{font-family:"Montserrat",sans-serif}
  .strip{position:absolute;left:14px;top:119px;display:flex;gap:8px}
  .card{position:relative;width:110px;height:138px;overflow:hidden;box-shadow:0 2px 6px rgba(0,0,0,.25)}
  .photo{position:absolute;inset:0}
  .copy{position:absolute;color:var(--white);text-transform:uppercase}
  .headline{font-weight:800;font-size:6.2px;line-height:.98;letter-spacing:.05px}
  .tagline{font-weight:700;font-size:4.4px;letter-spacing:.9px;margin-top:5px}
  .handle{font-weight:500;font-size:3.4px;color:var(--handle);text-transform:none;margin-top:9px}
  .center{text-align:center;left:6px;right:6px;bottom:8px}
  .left{left:9px;width:56px}
  .right{right:4px;width:50px}
  .muted{color:var(--muted)}
  .lav{color:var(--lavender)}
  .olive{color:var(--olive)}
  .pink{color:var(--pink)}
  .rose{color:var(--rose)}
  .tan{color:var(--tan)}
</style>
</head>
<body>
<main class="strip">

  <article class="card">
    <div class="photo" role="img" aria-label="Photo of the host smiling courtside in a crowded arena, holding a basketball" style="background:linear-gradient(180deg,#6e6a85 0%,#3d3f6e 45%,#1e2457 75%,#151a4a 100%)"></div>
    <div class="copy center">
      <p class="headline"><span class="lav">Tired. Moody.<br>Stubborn belly fat.</span><br>Your hormones are<br>screaming for help!</p>
      <p class="tagline">Let’s fix that.</p>
      <p class="handle">@TKBarlowOnline</p>
    </div>
  </article>

  <article class="card">
    <div class="photo" role="img" aria-label="Photo of the host in a sheer black top posing by a doorway" style="background:linear-gradient(90deg,#1f1f1f 0%,#2b2b2b 45%,#4a4644 70%,#2e2b2a 100%)"></div>
    <div class="copy left" style="top:29px">
      <p class="headline"><span class="muted">That<br>stubborn<br>weight?<br>It’s not<br>your fault.</span><br>Your<br>hormones<br>are to blame<br>and you’re<br>not alone;</p>
      <p class="tagline" style="margin-top:8px">But there<br>is a fix.</p>
      <p class="handle" style="margin-top:9px">@TKBarlowOnline</p>
    </div>
  </article>

  <article class="card">
    <div class="photo" role="img" aria-label="Photo of the host smiling outdoors in a black top against greenery" style="background:linear-gradient(90deg,#3a3d36 0%,#2d302b 40%,#232620 70%,#1d1f1c 100%)"></div>
    <div class="copy right" style="top:27px">
      <p class="headline"><span class="olive">Your<br>belly isn’t<br>fat…</span><br>It’s<br>hormonal.<br>And here’s<br>how to<br>fix it.</p>
      <p class="headline" style="margin-top:5px">Comment<br><span class="olive">hormones</span><br>if nothing<br>is working.</p>
      <p class="handle" style="margin-top:8px">@TKBarlowOnline</p>
    </div>
  </article>

  <article class="card">
    <div class="photo" role="img" aria-label="Photo of the host in a pink gown on a purple-lit stage" style="background:linear-gradient(90deg,#3a2550 0%,#4b2b63 45%,#6a2f6e 75%,#9b3a8a 100%)"></div>
    <div class="copy left" style="top:29px">
      <p class="headline"><span class="muted">The<br>stubborn<br>belly fat<br>after 40?</span><br>It’s not<br>about<br>calories;<br>it’s about<br>your<br>hormones.</p>
      <p class="tagline" style="margin-top:8px">Here is the fix!</p>
      <p class="handle" style="margin-top:9px">@TKBarlowOnline</p>
    </div>
  </article>

  <article class="card">
    <div class="photo" role="img" aria-label="Photo of the host in a kitchen pointing at her waist" style="background:linear-gradient(180deg,#4a3a30 0%,#3a2e27 40%,#2a2420 75%,#231e1b 100%)"></div>
    <div class="copy center">
      <p class="headline"><span class="muted">Flat tummy<br>in your 40s?</span><br>It’s still possible!<br>Comment <span class="rose">Bye Belly</span><br>to get the 10 secrets</p>
      <p class="tagline">To a flatter tummy</p>
      <p class="handle">@TKBarlowOnline</p>
    </div>
  </article>

  <article class="card">
    <div class="photo" role="img" aria-label="Photo of the host in a pink dress beside a sunflower display" style="background:linear-gradient(90deg,#5e5050 0%,#4a3236 40%,#3a1f28 70%,#2f1a22 100%)"></div>
    <div class="copy right" style="top:30px">
      <p class="headline"><span class="pink">Bloating.<br>Muffin top.<br>Puffy<br>waistline.</span><br>Your<br>body’s<br>screaming<br>for a<br>different<br>kind of fix.</p>
      <p class="tagline" style="margin-top:7px">Here it is.</p>
      <p class="handle" style="margin-top:9px">@TKBarlowOnline</p>
    </div>
  </article>

  <article class="card">
    <div class="photo" role="img" aria-label="Photo of the host dancing in a bright kitchen in a white crop top" style="background:linear-gradient(180deg,#bdbcbb 0%,#8a8887 35%,#3e3d3d 70%,#262626 100%)"></div>
    <div class="copy center">
      <p class="headline"><span class="muted">You’re doing<br>all the “right” things,</span><br>but your belly<br>won’t go down?<br>Here’s what</p>
      <p class="tagline" style="margin-top:3px">You haven’t tried.</p>
      <p class="handle">@TKBarlowOnline</p>
    </div>
  </article>

  <article class="card">
    <div class="photo" role="img" aria-label="Photo of the host in a black outfit standing outdoors" style="background:linear-gradient(90deg,#4b4f50 0%,#353839 40%,#262728 70%,#1f1f1f 100%)"></div>
    <div class="copy right" style="top:24px">
      <p class="headline"><span class="tan">This<br>90-day<br>plan helped<br>women<br>over 40</span><br>slim down,<br>get a tiny<br>waist and<br>feel sexy<br>again.</p>
      <p class="tagline" style="margin-top:7px">You’re next.</p>
      <p class="handle" style="margin-top:9px">@TKBarlowOnline</p>
    </div>
  </article>

  <article class="card">
    <div class="photo" role="img" aria-label="Photo of the host in a sheer black top posing indoors" style="background:linear-gradient(90deg,#1f1f1f 0%,#262626 45%,#3f3c3b 70%,#2a2827 100%)"></div>
    <div class="copy left" style="top:24px">
      <p class="headline"><span class="tan">This is<br>the secret<br>women<br>over 40</span><br>are using<br>to get<br>snatched;<br>without<br>starving.</p>
      <p class="headline" style="margin-top:5px">Comment<br><span class="tan">skinny</span><br>to get the<br>exact plan.</p>
      <p class="handle" style="margin-top:9px">@TKBarlowOnline</p>
    </div>
  </article>

  <article class="card">
    <div class="photo" role="img" aria-label="Photo of the host in black posing by a window over a night city view" style="background:linear-gradient(90deg,#4a3b33 0%,#33302f 40%,#252322 70%,#1d1b1a 100%)"></div>
    <div class="copy right" style="top:21px">
      <p class="headline"><span class="tan">What<br>worked<br>in your<br>30s</span><br>won’t<br>work now.<br>Here’s<br>what<br>actually<br>does.</p>
      <p class="headline" style="margin-top:5px">Drop<br><span class="tan">30 pounds</span><br>in 3 months.</p>
      <p class="handle" style="margin-top:9px">@TKBarlowOnline</p>
    </div>
  </article>

</main>
</body>
</html>
```